Create business card template

I need to create a simple, elegant and minimalistic business card template that I can use for also future people, so not only just for me.

I want ideas for it and to be quite printer friendly! I already have the company logo in vectorial format ant that has to be used in the business card format. I envision a black minimalistic design with a QR code. I accept all kind of ideas, metal or finishes in different looking materials, but I want to avoid wood or something that resembles old stuff. I need something modern, fresh and something that's in tune with out digital world since the QR code idea.

I need the end result in many known file formats and mandatory vectorial !! The size should be the same with a credit card, so no weird looking aspects.

THE IDEA HAS TO BE ORIGINAL! So please don't rush into business card software templates and in 2 minutes propose!

I'm willing to negotiate on the price if the idea is done from scratch and is completely original and much thought has been put into the work. I also uploaded a logo of the site to give you an idea!

```html
<!DOCTYPE html>
<html lang="en">
<head>
<meta charset="utf-8">
<title>Nordvale Business Card</title>
<link rel="stylesheet" href="https://fonts.googleapis.com/css2?family=Montserrat:wght@400;500;700&display=swap">
<style>
  :root {
    --stage: #2a2e35;
    --card: #121314;
    --card-edge: #1c1d1f;
    --accent: #2f8fd8;
    --brand-blue: #3d4fd0;
    --ink: #f2f2f2;
    --muted: #a9abae;
    --silver: #8e9195;
    --emboss: #1a1b1d;
  }
  * { box-sizing: border-box; margin: 0; padding: 0; }
  html, body { width: 1200px; height: 900px; overflow: hidden; }
  body {
    background: var(--stage);
    font-family: "Montserrat", sans-serif;
    display: flex;
    align-items: center;
    justify-content: center;
    gap: 40px;
  }
  .card {
    position: relative;
    width: 540px;
    height: 340px;
    background: var(--card);
    border: 1px solid var(--card-edge);
    border-radius: 18px;
    overflow: hidden;
  }

  /* Front */
  .emboss-disc {
    position: absolute;
    width: 230px; height: 230px;
    right: 40px; bottom: -70px;
    border-radius: 50%;
    background: var(--emboss);
  }
  .contact-rail {
    position: absolute;
    left: 40px; top: 40px;
    width: 2px; height: 190px;
    background: var(--accent);
  }
  .contact-rail::before {
    content: "";
    position: absolute;
    left: -3px; top: -4px;
    width: 8px; height: 8px;
    border-radius: 50%;
    background: var(--accent);
  }
  .identity { position: absolute; left: 58px; top: 34px; }
  .person-name {
    font-size: 20px; font-weight: 700; letter-spacing: 0.5px;
    color: var(--ink); text-transform: uppercase;
  }
  .person-name .first { color: var(--accent); }
  .person-role { font-size: 12px; color: var(--muted); margin-top: 2px; }
  .contact-list { position: absolute; left: 31px; top: 100px; list-style: none; }
  .contact-item {
    display: flex; align-items: flex-start; gap: 12px;
    font-size: 12px; line-height: 17px; color: var(--muted);
    margin-bottom: 10px;
  }
  .contact-icon {
    flex: none; width: 20px; height: 20px; border-radius: 50%;
    background: var(--accent);
    display: flex; align-items: center; justify-content: center;
  }
  .contact-icon svg { width: 12px; height: 12px; fill: #fff; }

  .brand { display: flex; align-items: center; gap: 10px; }
  .brand-dot { width: 22px; height: 22px; border-radius: 50%; }
  .brand-name { font-size: 26px; font-weight: 500; letter-spacing: 2px; }
  .front .brand { position: absolute; right: 40px; top: 130px; }
  .front .brand-dot { background: var(--brand-blue); }
  .front .brand-name { color: var(--brand-blue); }

  /* Back */
  .back { display: flex; flex-direction: column; align-items: center; justify-content: center; gap: 34px; }
  .back .brand-dot { background: var(--silver); width: 28px; height: 28px; }
  .back .brand-name { color: var(--silver); font-size: 34px; }
  .web-line { display: flex; align-items: center; gap: 14px; font-size: 12px; color: var(--silver); letter-spacing: 1px; }
  .web-line .rule { width: 110px; height: 2px; }
  .web-line .rule.left { background: linear-gradient(90deg, transparent, var(--silver)); }
  .web-line .rule.right { background: linear-gradient(90deg, var(--silver), transparent); }
</style>
</head>
<body>
  <section class="card front">
    <div class="emboss-disc"></div>
    <div class="contact-rail"></div>
    <div class="identity">
      <h1 class="person-name"><span class="first">Marcus</span> Ellery</h1>
      <p class="person-role">CEO/Founder</p>
    </div>
    <ul class="contact-list">
      <li class="contact-item">
        <span class="contact-icon"><svg viewBox="0 0 24 24"><path d="M12 2a7 7 0 0 0-7 7c0 5 7 13 7 13s7-8 7-13a7 7 0 0 0-7-7zm0 9.5A2.5 2.5 0 1 1 12 6.5a2.5 2.5 0 0 1 0 5z"/></svg></span>
        <span>1180 Harbor Ln 300<br>Westfield CA 5120 USA</span>
      </li>
      <li class="contact-item">
        <span class="contact-icon"><svg viewBox="0 0 24 24"><path d="M6.6 10.8a15 15 0 0 0 6.6 6.6l2.2-2.2a1 1 0 0 1 1-.25 11.4 11.4 0 0 0 3.6.6 1 1 0 0 1 1 1V20a1 1 0 0 1-1 1A17 17 0 0 1 3 4a1 1 0 0 1 1-1h3.5a1 1 0 0 1 1 1c0 1.25.2 2.45.6 3.6a1 1 0 0 1-.25 1z"/></svg></span>
        <span>0771205584</span>
      </li>
      <li class="contact-item">
        <span class="contact-icon"><svg viewBox="0 0 24 24"><path d="M3 5h18v14H3zm2 2v.5l7 4.5 7-4.5V7l-7 4.5z"/></svg></span>
        <span>hello@nordvale.co.za</span>
      </li>
      <li class="contact-item">
        <span class="contact-icon"><svg viewBox="0 0 24 24"><path d="M12 2a10 10 0 1 0 0 20 10 10 0 0 0 0-20zm0 2c.9 1.2 1.6 2.6 2 4h-4c.4-1.4 1.1-2.8 2-4zM4.3 14a8 8 0 0 1 0-4h3.4a16 16 0 0 0 0 4zm5.7 0a14 14 0 0 1 0-4h4a14 14 0 0 1 0 4zm6.3 0a16 16 0 0 0 0-4h3.4a8 8 0 0 1 0 4z"/></svg></span>
        <span>www.nordvale.co.za</span>
      </li>
    </ul>
    <div class="brand">
      <span class="brand-dot"></span>
      <span class="brand-name">NORDVALE</span>
    </div>
  </section>

  <section class="card back">
    <div class="brand">
      <span class="brand-dot"></span>
      <span class="brand-name">NORDVALE</span>
    </div>
    <div class="web-line">
      <span class="rule left"></span>
      <span>www.nordvale.co.za</span>
      <span class="rule right"></span>
    </div>
  </section>
</body>
</html>
```